Reggae Single iTunes Coverart

I need digital iTunes/Spotify cover art for a reggae single called Palmshade from my band Copper Lantern. I took a neat picture in the studio that perhaps could be incorporated, but not required.

Target Market(s)

Reggae music lovers.

Industry/Entity Type

Digital

Requirements
Must have
• My Copper Lantern guy needs to be incorporated into this.

```html
<!DOCTYPE html>
<html lang="en">
<head>
<meta charset="utf-8">
<title>Palmshade – Copper Lantern</title>
<link rel="stylesheet" href="https://fonts.googleapis.com/css2?family=Bungee&family=Didact+Gothic&display=swap">
<style>
  :root {
    --paper: #ffffff;
    --rasta-green: #1fa23a;
    --rasta-yellow: #f4e21c;
    --rasta-red: #e0261b;
    --outline: #111111;
    --shadow: #a9a9a9;
    --ink: #1a1a1a;
    --figure-light: #f3f3f3;
    --figure-dark: #dcdcdc;
  }
  html, body {
    margin: 0;
    padding: 0;
    overflow: hidden;
    background: var(--paper);
  }
  .cover {
    position: relative;
    width: 1200px;
    height: 1000px;
    background: var(--paper);
    overflow: hidden;
  }
  .cover-art {
    position: absolute;
    inset: 0;
  }
  .single-title {
    font-family: "Bungee", "Arial Black", sans-serif;
    font-size: 182px;
  }
  .single-title-shadow {
    fill: var(--shadow);
  }
  .single-title-face {
    fill: url(#rasta-stripes);
    stroke: var(--outline);
    stroke-width: 5px;
    paint-order: stroke fill;
  }
  .band-name {
    position: absolute;
    left: 0;
    width: 1228px;
    top: 552px;
    margin: 0;
    text-align: center;
    font-family: "Didact Gothic", "Helvetica", sans-serif;
    font-weight: 400;
    font-size: 34px;
    letter-spacing: 1px;
    color: var(--ink);
  }
  .band-mascot {
    position: absolute;
    left: 880px;
    top: 628px;
    width: 270px;
    height: 352px;
    background: linear-gradient(180deg, var(--figure-light), var(--figure-dark));
  }
</style>
</head>
<body>
  <main class="cover">
    <svg class="cover-art" width="1200" height="1000" viewBox="0 0 1200 1000" aria-hidden="true">
      <defs>
        <linearGradient id="rasta-stripes" x1="0" y1="400" x2="0" y2="532" gradientUnits="userSpaceOnUse">
          <stop offset="0" stop-color="var(--rasta-green)"/>
          <stop offset="0.36" stop-color="var(--rasta-green)"/>
          <stop offset="0.36" stop-color="var(--rasta-yellow)"/>
          <stop offset="0.66" stop-color="var(--rasta-yellow)"/>
          <stop offset="0.66" stop-color="var(--rasta-red)"/>
          <stop offset="1" stop-color="var(--rasta-red)"/>
        </linearGradient>
      </defs>
      <g class="single-title">
        <text class="single-title-shadow" x="197" y="544" textLength="848" lengthAdjust="spacingAndGlyphs">PALMSHADE</text>
        <text class="single-title-face" x="183" y="530" textLength="848" lengthAdjust="spacingAndGlyphs">PALMSHADE</text>
      </g>
    </svg>
    <h2 class="band-name">Copper Lantern</h2>
    <div class="band-mascot" role="img" aria-label="Copper Lantern band mascot: a cartoon guy holding a bottle and a cigarette"></div>
  </main>
</body>
</html>
```